Velisa Seafood Shipping Packaging Re-Design

We need a packaging (Shipping Carton) design for our Seafood Products (FROZEN). We already have a basic packaging design which we prefer to have a modern touch on it.
Spec :
1. It must show our logo (Attached), note that the text of "VELISA" which accompany the logo is optional, it can be omitted & showing only the logo.
2. Main color is Blue
3. Our carton is regular shipping box with dimension L43cm x W 27cm x H 16cm.
4. Our material of Carton is both Brown & White Kraft Paperboard, so the design should look nice in both material.

Attached our Logo and packaging design.

Target Market(s)

Frozen Seafood Distributor & Seafood Buyer

Industry/Entity Type

Food Production

Requirements
Must have
• 1. Must Show our Logo
• 2. Main Color of the Text/Logo is Blue
• 3. On the side of the packaging / Carton must show two box of CODE & SIZE
• 4. Must Show these icons :
• a. Handle with Care
• b. Maximum Stackable 10 Carton
• c. Recyleable Material
• d. Protect from the Water/Rain
Nice to have
• Would prefer to have a modern design

```html
<!DOCTYPE html>
<html lang="en">
<head>
<meta charset="utf-8">
<title>Velisa Shipping Carton Dieline</title>
<link rel="stylesheet" href="https://fonts.googleapis.com/css2?family=Lato:wght@400;700&display=swap">
<style>
:root{
  --deep-blue:#0a6aa6;
  --band-blue:#a8d5ee;
  --navy:#223266;
  --line:#8a8a8a;
  --paper:#ffffff;
}
*{margin:0;padding:0;box-sizing:border-box}
html,body{width:1200px;height:1000px;overflow:hidden;background:var(--paper)}
body{position:relative;font-family:"Lato",sans-serif;color:var(--navy)}
.panel{position:absolute;border:1px solid var(--line);background:var(--paper)}
.flap-bar{position:absolute;left:-1px;right:-1px;top:-1px;height:10px;background:var(--deep-blue)}
.band{position:absolute;left:54px;top:174px;width:1124px;height:127px;background:var(--band-blue)}
.glue-tab{position:absolute;left:28px;top:174px;width:36px;height:127px}
.band-mark{position:absolute;width:10px;background:var(--deep-blue)}
.brand{position:absolute;display:flex;align-items:center;gap:8px;color:var(--deep-blue);font-weight:700;transform:translate(-50%,-50%)}
.brand-dot{width:26px;height:26px;border:3px solid var(--deep-blue);border-radius:50%}
.brand-name{font-size:22px}
.wordmark{position:absolute;font-size:30px;font-weight:400;letter-spacing:6px;color:var(--navy);transform:translate(-50%,-50%)}
.wordmark.inverted{transform:translate(-50%,-50%) rotate(180deg)}
.info-box{position:absolute;border:1px solid var(--deep-blue)}
.info-box .divider{position:absolute;left:0;right:0;top:50%;border-top:1px solid var(--deep-blue)}
.spec-box{position:absolute;width:91px;height:82px;border:1px solid var(--deep-blue)}
.spec-box h3{height:19px;border-bottom:1px solid var(--deep-blue);font-size:13px;font-weight:700;letter-spacing:1.5px;text-align:center;line-height:18px;color:var(--deep-blue)}
.icon{position:absolute;width:26px;height:26px;border:1px solid var(--deep-blue);display:flex;align-items:center;justify-content:center}
.icon svg{width:20px;height:20px}
.thermo{position:absolute}
</style>
</head>
<body>

<!-- top flaps -->
<section class="panel" style="left:56px;top:46px;width:341px;height:128px">
  <div class="flap-bar"></div>
  <div class="wordmark inverted" style="left:170px;top:68px">VELISA</div>
</section>
<section class="panel" style="left:399px;top:46px;width:216px;height:128px">
  <div class="brand" style="left:108px;top:64px"><span class="brand-dot"></span><span class="brand-name">Velisa</span></div>
</section>
<section class="panel" style="left:618px;top:46px;width:341px;height:128px">
  <div class="flap-bar"></div>
  <div class="info-box" style="left:13px;top:17px;width:129px;height:98px"><div class="divider"></div></div>
  <svg class="thermo" style="left:292px;top:24px;transform:rotate(180deg)" width="30" height="82" viewBox="0 0 30 82">
    <rect x="7" y="0" width="16" height="66" rx="8" fill="var(--band-blue)"/>
    <rect x="12" y="36" width="6" height="28" rx="3" fill="var(--deep-blue)"/>
    <circle cx="15" cy="67" r="14" fill="var(--band-blue)"/>
    <circle cx="15" cy="67" r="10" fill="var(--deep-blue)"/>
    <text x="15" y="69" font-size="6" font-family="Lato,sans-serif" font-weight="700" fill="#fff" text-anchor="middle">-18°C</text>
  </svg>
</section>
<section class="panel" style="left:961px;top:46px;width:216px;height:128px">
  <div class="brand" style="left:108px;top:64px"><span class="brand-dot"></span><span class="brand-name">Velisa</span></div>
</section>

<!-- body band -->
<svg class="glue-tab" viewBox="0 0 36 127" aria-hidden="true">
  <polygon points="0,12 26,0 36,0 36,127 26,127 0,115" fill="var(--deep-blue)"/>
</svg>
<div class="band">
  <div class="brand" style="left:179px;top:62px"><span class="brand-dot"></span><span class="brand-name">Velisa</span></div>
  <div class="brand" style="left:741px;top:62px"><span class="brand-dot"></span><span class="brand-name">Velisa</span></div>
</div>
<div class="band-mark" style="left:54px;top:198px;height:86px"></div>
<div class="band-mark" style="left:388px;top:198px;height:85px"></div>
<div class="band-mark" style="left:616px;top:198px;height:85px"></div>
<div class="band-mark" style="left:949px;top:196px;height:84px"></div>

<!-- bottom flaps -->
<section class="panel" style="left:56px;top:302px;width:341px;height:128px">
  <svg class="thermo" style="left:15px;top:22px" width="30" height="82" viewBox="0 0 30 82">
    <rect x="7" y="0" width="16" height="66" rx="8" fill="var(--band-blue)"/>
    <rect x="12" y="36" width="6" height="28" rx="3" fill="var(--deep-blue)"/>
    <circle cx="15" cy="67" r="14" fill="var(--band-blue)"/>
    <circle cx="15" cy="67" r="10" fill="var(--deep-blue)"/>
    <text x="15" y="69" font-size="6" font-family="Lato,sans-serif" font-weight="700" fill="#fff" text-anchor="middle">-18°C</text>
  </svg>
  <div class="info-box" style="left:197px;top:12px;width:129px;height:98px"><div class="divider"></div></div>
</section>

<section class="panel" style="left:399px;top:302px;width:216px;height:128px">
  <div class="spec-box" style="left:10px;top:6px"><h3>CODE</h3></div>
  <div class="spec-box" style="left:113px;top:6px"><h3>SIZE</h3></div>
  <div class="icon" style="left:25px;top:94px"><svg viewBox="0 0 20 20" fill="none" stroke="var(--deep-blue)" stroke-width="1.4"><path d="M3 10a7 6 0 0 1 14 0z" fill="var(--deep-blue)"/><path d="M10 10v6a2 2 0 0 1-4 0"/><path d="M6 3l-1-2M10 2V0M14 3l1-2"/></svg></div>
  <div class="icon" style="left:59px;top:94px"><svg viewBox="0 0 20 20" fill="var(--deep-blue)"><path d="M2 6l3 0 2 7 3 2 3-2 2-7 3 0-2 9-6 4-6-4z"/><rect x="8" y="3" width="4" height="6"/></svg></div>
  <div class="icon" style="left:128px;top:94px"><svg viewBox="0 0 20 20"><text x="10" y="11" font-size="10" font-weight="700" font-family="Lato,sans-serif" fill="var(--deep-blue)" text-anchor="middle">10</text><path d="M3 14h14M3 17h14" stroke="var(--deep-blue)" stroke-width="1.4"/></svg></div>
  <div class="icon" style="left:162px;top:94px"><svg viewBox="0 0 20 20" fill="none" stroke="var(--deep-blue)" stroke-width="2"><path d="M7 4l3-2 3 5"/><path d="M17 11l1 4h-6"/><path d="M6 17H2l2-5"/></svg></div>
</section>

<section class="panel" style="left:618px;top:302px;width:341px;height:128px">
  <div class="wordmark" style="left:170px;top:66px">VELISA</div>
</section>

<section class="panel" style="left:961px;top:302px;width:216px;height:128px">
  <div class="spec-box" style="left:10px;top:6px"><h3>CODE</h3></div>
  <div class="spec-box" style="left:113px;top:6px"><h3>SIZE</h3></div>
  <div class="icon" style="left:25px;top:94px"><svg viewBox="0 0 20 20" fill="none" stroke="var(--deep-blue)" stroke-width="1.4"><path d="M3 10a7 6 0 0 1 14 0z" fill="var(--deep-blue)"/><path d="M10 10v6a2 2 0 0 1-4 0"/><path d="M6 3l-1-2M10 2V0M14 3l1-2"/></svg></div>
  <div class="icon" style="left:59px;top:94px"><svg viewBox="0 0 20 20" fill="var(--deep-blue)"><path d="M2 6l3 0 2 7 3 2 3-2 2-7 3 0-2 9-6 4-6-4z"/><rect x="8" y="3" width="4" height="6"/></svg></div>
  <div class="icon" style="left:128px;top:94px"><svg viewBox="0 0 20 20"><text x="10" y="11" font-size="10" font-weight="700" font-family="Lato,sans-serif" fill="var(--deep-blue)" text-anchor="middle">10</text><path d="M3 14h14M3 17h14" stroke="var(--deep-blue)" stroke-width="1.4"/></svg></div>
  <div class="icon" style="left:162px;top:94px"><svg viewBox="0 0 20 20" fill="none" stroke="var(--deep-blue)" stroke-width="2"><path d="M7 4l3-2 3 5"/><path d="M17 11l1 4h-6"/><path d="M6 17H2l2-5"/></svg></div>
</section>

</body>
</html>
```